Varden Institute for Restorative Care

I need a full informational website for my medical practice. I would like to use my logo and also include a lot of emblems/pictures (also a picture of me in a white coat). The website should have a function for people to inquire and send me messages. I will be offering needle-less regenerative injection therapy, stem cell treatments, bioidentical hormone therapy, treatment for chronic illness, neurodegenerative diseases, skin rejuvenation, hair restoration, male enhancement, female enhancement, and anti-aging. The practice will not be accepting insurance and will be cash/credit card only.
A good example of written content and functionality is this website:
http://thebrvx.example/. However, I want different theme and tones.
Target Market(s)
High end clientele in Los Angeles, Southern California. Health minded people who are interested in living better and longer and can afford anti-aging treatments. Men and women who want to improve sexual health and wellbeing.
Requirements
Must have
- 1. I will need to be able to move the site to other servers (needed for site speed)
- 2. Site must be build on WordPress
- 3. Full admin credentials for domain, cpanel, wordpress, ftp.
- 4. No third party interaction on development and content deployment once the site is on different servers
- 5. I will need the ability to add content and links to the site
- 6. I will need the ability to optimize the site for speed
- 7. I will need to ability to modify URLs so they are more SEO friendly
Nice to have
- pictures of stem cells, health improvement and regeneration, beauty, youthful individuals, older healthy and happy individuals. Medical designs.
Should not have
- flowers, dna

```html
<!DOCTYPE html>
<html lang="en">
<head>
<meta charset="utf-8">
<title>Varden Institute for Restorative Care</title>
<link rel="stylesheet" href="https://fonts.googleapis.com/css2?family=Montserrat:wght@400;500;600;700&display=swap">
<style>
  :root {
    --navy: #14206e;
    --ink: #3a3f55;
    --muted: #6b7080;
    --green: #22a782;
    --band: #1f3d94;
    --band-dark: #132c78;
    --pale: #eef7fa;
    --white: #ffffff;
    --field: #ffffff;
  }
  * { box-sizing: border-box; margin: 0; padding: 0; }
  html, body { width: 1200px; height: 2375px; overflow: hidden; }
  body { font-family: "Montserrat", sans-serif; color: var(--ink); background: var(--pale); position: relative; }

  .arrow-link { position: absolute; display: flex; align-items: center; height: 50px; font-size: 11.5px; font-weight: 600; letter-spacing: 1.2px; text-transform: uppercase; color: var(--ink); text-decoration: none; }
  .arrow-link svg { position: absolute; left: 0; top: 0; }
  .arrow-link span { margin-left: 44px; }
  .arrow-link.light { color: var(--white); }

  /* header + hero */
  .hero { position: absolute; left: 0; top: 0; width: 1200px; height: 563px; background: linear-gradient(100deg, #f4f7f9 0%, #e6ecef 45%, #d9e1e6 70%, #c9d3da 100%); }
  .hero-portrait { position: absolute; left: 590px; top: 110px; width: 480px; height: 453px; background: radial-gradient(ellipse at 50% 40%, #d8c2b0 0%, #c7cfd8 45%, rgba(200,210,220,0) 75%); }
  .brand { position: absolute; left: 76px; top: 52px; display: flex; align-items: center; gap: 12px; }
  .brand-dot { width: 30px; height: 30px; border-radius: 50%; background: var(--green); }
  .brand-name { font-size: 30px; font-weight: 700; letter-spacing: 1px; color: var(--navy); }
  .nav { position: absolute; left: 396px; top: 66px; display: flex; gap: 22px; font-size: 13.5px; color: var(--ink); }
  .nav a { color: inherit; text-decoration: none; }
  .nav .phone { font-weight: 700; color: var(--navy); }
  .inquire { position: absolute; left: 978px; top: 52px; width: 146px; height: 42px; border: 1.5px solid var(--green); border-radius: 21px; display: flex; align-items: center; justify-content: center; font-size: 11.5px; font-weight: 600; letter-spacing: 1px; color: var(--green); text-decoration: none; }
  .hero-title { position: absolute; left: 158px; top: 248px; font-size: 38px; line-height: 42px; font-weight: 700; letter-spacing: 1.5px; color: var(--navy); text-transform: uppercase; }

  /* profile band */
  .profile { position: absolute; left: 0; top: 563px; width: 1200px; height: 442px; background: radial-gradient(circle at 50% 100%, #3356ad 0%, var(--band) 35%, var(--band-dark) 100%); color: var(--white); text-align: center; }
  .profile h2 { position: absolute; top: 114px; width: 100%; font-size: 30px; font-weight: 700; letter-spacing: 1.5px; }
  .profile .role { position: absolute; top: 150px; width: 100%; font-size: 20px; font-weight: 400; }
  .profile p { position: absolute; left: 228px; top: 196px; width: 744px; font-size: 12.5px; line-height: 16px; }

  /* practice */
  .practice-head { position: absolute; left: 0; top: 1005px; width: 1200px; height: 162px; background: var(--pale); }
  .practice-head h2 { position: absolute; left: 150px; top: 64px; font-size: 30px; font-weight: 700; letter-spacing: 1.5px; color: var(--navy); }
  .cards { position: absolute; left: 0; top: 1167px; width: 1200px; height: 443px; display: flex; }
  .card { position: relative; width: 300px; height: 443px; color: var(--white); }
  .card-1 { background: linear-gradient(160deg, #d9b7a3 0%, #8a6a5c 60%, #3c2f2e 100%); }
  .card-2 { background: linear-gradient(160deg, #6b6e74 0%, #3e3b3a 60%, #26272b 100%); }
  .card-3 { background: linear-gradient(160deg, #5a6650 0%, #2b2a33 55%, #1c1b24 100%); }
  .card-4 { background: linear-gradient(160deg, #e8dcd4 0%, #b59b8c 55%, #6e564c 100%); }
  .card::after { content: ""; position: absolute; inset: 0; background: linear-gradient(180deg, rgba(0,0,0,0) 35%, rgba(0,0,0,.45) 100%); }
  .card > * { z-index: 1; }
  .card h3 { position: absolute; left: 40px; top: 220px; width: 210px; font-size: 14px; line-height: 18px; font-weight: 700; letter-spacing: .8px; text-transform: uppercase; }
  .card p { position: absolute; left: 40px; top: 272px; width: 190px; font-size: 12px; line-height: 18px; }
  .card .arrow-link { left: 40px; top: 364px; color: var(--white); }
  .btn-fill { position: absolute; left: 40px; top: 369px; width: 144px; height: 42px; border-radius: 21px; background: var(--green); display: flex; align-items: center; justify-content: center; font-size: 11.5px; font-weight: 600; letter-spacing: 1px; color: var(--white); text-decoration: none; }

  /* contact */
  .contact { position: absolute; left: 0; top: 1610px; width: 1200px; height: 483px; background: var(--pale); }
  .contact h2 { position: absolute; top: 60px; width: 100%; text-align: center; font-size: 30px; font-weight: 700; letter-spacing: 1.5px; color: var(--navy); }
  .address { position: absolute; left: 152px; top: 156px; font-style: normal; }
  .address strong { display: block; font-size: 14px; font-weight: 600; color: var(--ink); margin-bottom: 6px; }
  .address .lines { font-size: 12px; line-height: 19px; color: var(--muted); }
  .address .tel { font-size: 20px; color: var(--muted); margin-top: 12px; }
  .address .mail { font-size: 12px; color: var(--muted); margin-top: 4px; }
  .social { display: flex; gap: 8px; margin-top: 26px; }
  .social span { width: 20px; height: 20px; border-radius: 50%; background: #b9bec6; }
  .field { position: absolute; background: var(--field); border: none; }
  .copyright { position: absolute; left: 152px; top: 384px; font-size: 11.5px; letter-spacing: .8px; color: var(--muted); }

  .map { position: absolute; left: 0; top: 2093px; width: 1200px; height: 282px; background: linear-gradient(135deg, #e4e4e4 0%, #d6d6d6 50%, #e9e9e9 100%); }
</style>
</head>
<body>

<header class="hero">
  <div class="hero-portrait" role="img" aria-label="Photo of the doctor in a white coat with a stethoscope, smiling, in a bright clinic"></div>
  <div class="brand"><span class="brand-dot"></span><span class="brand-name">VARDEN</span></div>
  <nav class="nav">
    <a href="#">Dr. Lorem Text</a>
    <a href="#">Medical Practice</a>
    <a href="#">Science</a>
    <a href="#">Contact</a>
    <a class="phone" href="#">P: +1 888 555 0142</a>
  </nav>
  <a class="inquire" href="#">INQUIRE NOW</a>
  <h1 class="hero-title">Varden Institute<br>for Restorative<br>Care</h1>
  <a class="arrow-link" href="#" style="left:152px;top:413px;">
    <svg width="40" height="50" viewBox="0 0 40 50"><path d="M24 2 A23 23 0 0 0 24 48" fill="none" stroke="#3a3f55" stroke-width="1.3"/><path d="M22 25 H34 M30 21 L34 25 L30 29" fill="none" stroke="#3a3f55" stroke-width="1.4"/></svg>
    <span>Contact me</span>
  </a>
</header>

<section class="profile" role="img" aria-label="Blue background of soft out-of-focus cells">
  <h2>DR. LOREM TEXT</h2>
  <div class="role">CEO of Varden Institute for Restorative Care.</div>
  <p>Lorem ipsum dolor sit amet, consectetur adipiscing elit, sed do eiusmod tempor incididunt ut labore et dolore magna aliqua. Ut enim ad minim veniam, quis nostrud exercitation ullamco laboris nisi ut aliquip ex ea commodo consequat. Duis aute irure dolor in reprehenderit in voluptate velit esse cillum dolore eu fugiat nulla pariatur. At vero eos et accusamus et iusto odio dignissimos ducimus qui blanditiis praesentium ...</p>
  <a class="arrow-link light" href="#" style="left:516px;top:316px;">
    <svg width="40" height="50" viewBox="0 0 40 50"><path d="M24 2 A23 23 0 0 0 24 48" fill="none" stroke="#ffffff" stroke-width="1.3"/><path d="M22 25 H34 M30 21 L34 25 L30 29" fill="none" stroke="#ffffff" stroke-width="1.4"/></svg>
    <span>Discover more</span>
  </a>
</section>

<section class="practice-head">
  <h2>MEDICAL PRACTICE</h2>
  <a class="arrow-link" href="#" style="left:902px;top:56px;">
    <svg width="40" height="50" viewBox="0 0 40 50"><path d="M24 2 A23 23 0 0 0 24 48" fill="none" stroke="#3a3f55" stroke-width="1.3"/><path d="M22 25 H34 M30 21 L34 25 L30 29" fill="none" stroke="#3a3f55" stroke-width="1.4"/></svg>
    <span>Explore all</span>
  </a>
</section>

<section class="cards">
  <article class="card card-1" role="img" aria-label="Woman with closed eyes receiving a relaxing facial treatment">
    <h3>Regenerative Injec-<br>tion Treatment</h3>
    <p>There are many variations of passages of Lorem Ipsum available, but the ...</p>
    <a class="arrow-link" href="#"><svg width="40" height="50" viewBox="0 0 40 50"><path d="M24 2 A23 23 0 0 0 24 48" fill="none" stroke="#ffffff" stroke-width="1.3"/><path d="M22 25 H34 M30 21 L34 25 L30 29" fill="none" stroke="#ffffff" stroke-width="1.4"/></svg><span>Learn more</span></a>
  </article>
  <article class="card card-2" role="img" aria-label="Therapist examining a patient's bandaged knee">
    <h3>Stem Cell Therapy and Treatment</h3>
    <p>There are many variations of passages of Lorem Ipsum available, but the ...</p>
    <a class="arrow-link" href="#"><svg width="40" height="50" viewBox="0 0 40 50"><path d="M24 2 A23 23 0 0 0 24 48" fill="none" stroke="#ffffff" stroke-width="1.3"/><path d="M22 25 H34 M30 21 L34 25 L30 29" fill="none" stroke="#ffffff" stroke-width="1.4"/></svg><span>Learn more</span></a>
  </article>
  <article class="card card-3" role="img" aria-label="Happy older couple outdoors">
    <h3>Bioidentical Hormone Therapy</h3>
    <p>There are many variations of passages of Lorem Ipsum available, but the ...</p>
    <a class="btn-fill" href="#">LEARN MORE</a>
  </article>
  <article class="card card-4" role="img" aria-label="Therapist giving a massage to a patient">
    <h3>Treatment for Chron-<br>ic Illness</h3>
    <p>There are many variations of passages of Lorem Ipsum available, but the ...</p>
    <a class="arrow-link" href="#"><svg width="40" height="50" viewBox="0 0 40 50"><path d="M24 2 A23 23 0 0 0 24 48" fill="none" stroke="#ffffff" stroke-width="1.3"/><path d="M22 25 H34 M30 21 L34 25 L30 29" fill="none" stroke="#ffffff" stroke-width="1.4"/></svg><span>Learn more</span></a>
  </article>
</section>

<section class="contact">
  <h2>CONTACT US</h2>
  <address class="address">
    <strong>Varden Institute</strong>
    <div class="lines">72 lorem ipsum simply dummy text,<br>Lorem Ipsum, CA 91311</div>
    <div class="tel">P. +1 888 555 0142</div>
    <div class="mail">E. hello@varden.example</div>
    <div class="social"><span></span><span></span><span></span><span></span></div>
  </address>
  <form>
    <input class="field" type="text" aria-label="Name" style="left:459px;top:161px;width:206px;height:41px;">
    <input class="field" type="email" aria-label="Email" style="left:681px;top:161px;width:204px;height:41px;">
    <input class="field" type="tel" aria-label="Phone" style="left:902px;top:161px;width:144px;height:41px;">
    <textarea class="field" aria-label="Message" style="left:459px;top:218px;width:587px;height:121px;resize:none;"></textarea>
  </form>
  <div class="copyright">© 2018 VARDEN.</div>
  <a class="arrow-link" href="#" style="left:459px;top:366px;">
    <svg width="40" height="50" viewBox="0 0 40 50"><path d="M24 2 A23 23 0 0 0 24 48" fill="none" stroke="#3a3f55" stroke-width="1.3"/><path d="M22 25 H34 M30 21 L34 25 L30 29" fill="none" stroke="#3a3f55" stroke-width="1.4"/></svg>
    <span>Explore all</span>
  </a>
</section>

<div class="map" role="img" aria-label="Grey street map showing the practice location"></div>

</body>
</html>
```